Eastward keel catch

Hi everyone,
I’m operating a fishing boat targeting sought after deep water fish species off the southern coast of wa, where the product is sold from the boat directly to restaurants around the region. We fish with rods and not nets ensuring the fish are caught in an eco friendly manner maintaining longevity of the industry. This fishery takes place along a rugged coastline and wild oceans where conditions are not always favourable. Hoping for a design that can encompass these elements and also the care taken during harvest of the product ensuring quality of the fish and freshest fillets. I’ve attached photos of some targeted species, blue eye trevalla and dhufish, nannigai and pink snapper which would be nice to include
Thanks marcus

Target Market(s)

Restaurants/ seafood processors

Contact Information for Business Card

Top quality line caught scalefish, sustainably sourced from the pristine waters of south west WA
Contact marcus holt 0417586204

Requirements
Must have
• Catchy design yet simple
Appealing and promote values of business
-premium quality and freshness
-minimal impact on environment
Nice to have
• The wa dhufish incorporated in the logo. Kestrelbaitco.example have a few good examples as theirs

```html
<!DOCTYPE html>
<html lang="en">
<head>
<meta charset="utf-8">
<title>Eastward Keel Catch — Business Card</title>
<link rel="stylesheet" href="https://fonts.googleapis.com/css2?family=Urbanist:wght@400;500;600;700&display=swap">
<style>
  :root {
    --page-bg: #f8f7f5;
    --card-bg: #ffffff;
    --ink-dark: #19213a;
    --ink-blue: #3f5878;
    --ink-soft: #4d6686;
    --fish-light: #e4eaf0;
    --fish-mid: #a9b8c8;
    --fish-deep: #5d7088;
  }
  * { box-sizing: border-box; margin: 0; padding: 0; }
  html, body {
    width: 1200px;
    height: 534px;
    overflow: hidden;
    background: var(--page-bg);
    font-family: "Urbanist", sans-serif;
  }
  .canvas {
    position: relative;
    width: 1200px;
    height: 534px;
  }
  .card {
    position: absolute;
    top: 121px;
    width: 510px;
    height: 291px;
    background: var(--card-bg);
  }
  .card--front { left: 66px; }
  .card--back { left: 605px; }
  .fish-artwork {
    width: 100%;
    height: 100%;
    background:
      radial-gradient(ellipse 40% 28% at 60% 30%, var(--fish-mid), transparent 70%),
      radial-gradient(ellipse 38% 26% at 25% 62%, var(--fish-mid), transparent 70%),
      radial-gradient(ellipse 30% 24% at 18% 10%, var(--fish-mid), transparent 70%),
      radial-gradient(ellipse 34% 24% at 78% 88%, var(--fish-mid), transparent 70%),
      linear-gradient(135deg, var(--fish-light), #ffffff 50%, var(--fish-light));
  }
  .contact {
    padding: 36px 0 0 35px;
  }
  .business-name {
    font-size: 23px;
    font-weight: 600;
    color: var(--ink-dark);
    line-height: 1.2;
  }
  .person-name {
    margin-top: 30px;
    font-size: 19px;
    font-weight: 500;
    color: var(--ink-blue);
    line-height: 1.3;
  }
  .contact-line {
    font-size: 17px;
    font-weight: 400;
    color: var(--ink-dark);
    line-height: 22px;
  }
  .tagline {
    margin-top: 32px;
    width: 384px;
    font-size: 17px;
    font-weight: 400;
    color: var(--ink-soft);
    line-height: 22px;
    text-align: justify;
  }
</style>
</head>
<body>
  <main class="canvas">
    <section class="card card--front">
      <div class="fish-artwork" role="img" aria-label="Engraved-style illustration of four striped dhufish swimming in a school, in blue-grey ink on white"></div>
    </section>
    <section class="card card--back">
      <div class="contact">
        <h1 class="business-name">Eastward Keel Catch</h1>
        <p class="person-name">Marcus Holt</p>
        <p class="contact-line">0417586204</p>
        <p class="contact-line">marcushhh@keelmail.example</p>
        <p class="tagline">Top quality line caught scalefish, sustainably harvested from the pristine waters of south west WA.</p>
      </div>
    </section>
  </main>
</body>
</html>
```